Clean and modern business cards

Looking for an updated business card design for my dental office “corvanta dental” . Looking for a modern clean / sleek design . I’m thinking black background but open to seeing other options . One side needs to have an appointment card . Card needs to have logo, dentist name , phone, email , address . I’ve attached couple of cards I thought were cool as well as my logo
Target Market(s)
Dental patients
Industry/Entity Type
Dentistry
Contact Information for Business Card
Phone email address

```html
<!DOCTYPE html>
<html lang="en">
<head>
<meta charset="UTF-8">
<title>Corvanta Dental – Business Card</title>
<link href="https://fonts.googleapis.com/css2?family=Montserrat:wght@400;500&display=swap" rel="stylesheet">
<style>
  :root {
    --page-bg: #ececec;
    --card-bg: #262626;
    --ink: #f2f2f2;
    --ink-soft: #e4e4e4;
    --accent: #22a9dc;
    --field: #ffffff;
  }
  * { box-sizing: border-box; margin: 0; padding: 0; }
  html, body {
    width: 800px; height: 1200px; overflow: hidden;
    background: var(--page-bg);
    font-family: "Montserrat", Arial, sans-serif;
    color: var(--ink);
  }
  .canvas { position: relative; width: 800px; height: 1200px; }
  .card {
    position: absolute; left: 40px; width: 720px; height: 412px;
    background: var(--card-bg);
  }
  .card--front { top: 150px; }
  .card--back  { top: 622px; }

  /* Front */
  .brand-mark {
    position: absolute; left: 60px; top: 96px; width: 220px; height: 220px;
    display: flex; flex-direction: column; align-items: center; justify-content: center; gap: 14px;
  }
  .brand-mark__dot {
    width: 26px; height: 26px; border-radius: 50%; background: var(--accent);
  }
  .brand-mark__name {
    font-size: 19px; font-weight: 500; letter-spacing: 3px; text-align: center; line-height: 1.4;
    color: var(--ink);
  }
  .dentist-name {
    position: absolute; left: 359px; top: 112px;
    font-size: 27px; font-weight: 400; letter-spacing: 2.2px;
  }
  .contact-list {
    position: absolute; left: 362px; top: 208px; list-style: none;
    font-size: 18.5px; letter-spacing: 0.6px; color: var(--ink-soft);
  }
  .contact-list li { display: flex; align-items: flex-start; gap: 14px; line-height: 24px; margin-bottom: 7px; }
  .contact-list svg { flex: none; width: 14px; height: 14px; margin-top: 5px; fill: var(--accent); }

  /* Back */
  .appointment__title {
    position: absolute; left: 59px; top: 50px;
    font-size: 18.5px; letter-spacing: 0.8px;
  }
  .appointment__row { position: absolute; left: 58px; display: flex; align-items: center; gap: 8px; }
  .appointment__row--date { top: 104px; }
  .appointment__row--time { top: 158px; }
  .appointment__label { width: 56px; font-size: 18.5px; letter-spacing: 0.6px; }
  .appointment__field { width: 310px; height: 32px; background: var(--field); }
  .back-mark {
    position: absolute; left: 470px; top: 60px; width: 200px; height: 160px;
    display: flex; align-items: center; justify-content: center; gap: 12px;
  }
  .back-mark__dot { width: 22px; height: 22px; border-radius: 50%; background: var(--accent); flex: none; }
  .back-mark__name { font-size: 18px; font-weight: 500; letter-spacing: 2.5px; line-height: 1.4; }
  .policy {
    position: absolute; left: 59px; top: 232px; width: 600px;
    font-size: 18.5px; line-height: 28px; letter-spacing: 0.4px; color: var(--ink-soft);
  }
  .practice-details {
    position: absolute; left: 59px; top: 304px;
    font-size: 18.5px; line-height: 32px; letter-spacing: 0.4px; color: var(--ink-soft);
  }
</style>
</head>
<body>
<main class="canvas">
  <section class="card card--front" aria-label="Business card front">
    <div class="brand-mark">
      <span class="brand-mark__dot"></span>
      <span class="brand-mark__name">CORVANTA<br>DENTAL</span>
    </div>
    <h1 class="dentist-name">MARCUS HALE</h1>
    <ul class="contact-list">
      <li>
        <svg viewBox="0 0 24 24" aria-hidden="true"><path d="M6.6 10.8c1.4 2.8 3.8 5.1 6.6 6.6l2.2-2.2c.3-.3.7-.4 1-.2 1.1.4 2.3.6 3.6.6.6 0 1 .4 1 1V20c0 .6-.4 1-1 1C10.6 21 3 13.4 3 4c0-.6.4-1 1-1h3.5c.6 0 1 .4 1 1 0 1.3.2 2.5.6 3.6.1.3 0 .7-.2 1l-2.3 2.2z"/></svg>
        <span>(204) 555-0172</span>
      </li>
      <li>
        <svg viewBox="0 0 24 24" aria-hidden="true"><path d="M2 5h20v14H2z" opacity=".9"/><path d="M2 5l10 8 10-8" fill="none" stroke="#262626" stroke-width="2"/></svg>
        <span>contact@corvantadental.ca</span>
      </li>
      <li>
        <svg viewBox="0 0 24 24" aria-hidden="true"><path d="M12 2a7 7 0 0 0-7 7c0 5.2 7 13 7 13s7-7.8 7-13a7 7 0 0 0-7-7zm0 9.5a2.5 2.5 0 1 1 0-5 2.5 2.5 0 0 1 0 5z"/></svg>
        <span>2480 Alder Ridge HWY<br>Winnipeg, MB</span>
      </li>
    </ul>
  </section>

  <section class="card card--back" aria-label="Appointment card back">
    <p class="appointment__title">YOUR NEXT APPOINTMENT IS</p>
    <div class="appointment__row appointment__row--date">
      <span class="appointment__label">DATE</span>
      <span class="appointment__field"></span>
    </div>
    <div class="appointment__row appointment__row--time">
      <span class="appointment__label">TIME</span>
      <span class="appointment__field"></span>
    </div>
    <div class="back-mark">
      <span class="back-mark__dot"></span>
      <span class="back-mark__name">CORVANTA<br>DENTAL</span>
    </div>
    <p class="policy">To cancel or reschedule please notify us atleast 48 hours<br>prior to your scheduled appointment</p>
    <p class="practice-details">2480 ALDER RIDGE HWY, WINNIPEG, MB &nbsp;|&nbsp; (204) 555-0172<br>CORVANTADENTAL.CA &nbsp;|&nbsp; CONTACT@CORVANTADENTAL.CA</p>
  </section>
</main>
</body>
</html>
```